Greek God inspired Air Freshen needs Foil Package Design

We are Lantern of Meridia. We sell car air fresheners inspired by Ancient Greece. We currently sell 5 proprietary scents. You can see them here: https://www.shopvarel.example/Freshener-Natural-Essential-Lantern-Meridia/dp/Q7K2MXR4PL
These are luxury air fresheners sold in awesome packages. 100% essential oils blended and bottled in the USA.
We need your help! We want to sell an additional line of scents. This line will be called "The Tidal Series" - or, The Tidal Series by Lantern of Meridia. This collection's theme will be - "The aromas you love, refined by the Fates."
These new products will be takes on well know colognes and perfumes.
We will start with 3 new products:
Halvir – inspired by Brisamel by Tolvane
Lemituna – inspired by Marindel by Quell
Pelund – inspired by Nevra by Faskow
Our original 5 products are packaged in tubes and bottled in a luxury black 8ml bottle (see attached and the link above). The "Tidal Series" will also have the same bottles, BUT, we want to package them in MYLAR FOIL BAGS. They will be 10x7cm (template attached).
What we need from you guys .... 3 designs. Front of the bag ONLY. One for each:
You have free reign, however the following items must be met:
The designs must be min 300 dpi.
Must include: "Tidal Series by Lantern of Meridia"
Must include: Lantern of Meridia Logo (attached)
Must include the words: "Car Air Fresheners"
Must marry well with our current imagery: https://www.shopvarel.example/Freshener-Natural-Essential-Lantern-Meridia/dp/Q7K2MXR4PL
Don't necessarily need to mention the cologne that our product is inspired by, however, perhaps consider use some fonts/pattern/s shadows of the Tolvane/Brsiamel bottle "shape" as an example.
Keep in mind, you are only designing the front of the packages. We will complete the back. The back will have the brand story, instructions, UPC, ingredients.
Our thoughts on using foil mylar bags: 1. We sell online 2. They will stand out from the others 3. Gives you/designer more space/opportunity to convey the product/message 4. We believe mock-ups/photos of the bags will look great on our listing
Please contact with any questions.

```html
<!DOCTYPE html>
<html lang="en">
<head>
<meta charset="utf-8">
<title>Pelund – Tidal Series – Car Air Fresheners</title>
<link rel="stylesheet" href="https://fonts.googleapis.com/css2?family=Advent+Pro:wght@300;400;600&family=Poiret+One&display=swap">
<style>
  :root {
    --stage: #e9e9ea;
    --violet-deep: #2a1150;
    --violet-dark: #3b1766;
    --violet-mid: #5a2b8c;
    --violet-bright: #9a3bc4;
    --orchid: #b55ad6;
    --lilac-pale: #e2c3ea;
    --lilac-mid: #b88ad0;
    --ink: #4a2470;
  }
  html, body {
    margin: 0;
    padding: 0;
    width: 1200px;
    height: 1001px;
    overflow: hidden;
    background: var(--stage);
  }
  .canvas {
    position: relative;
    width: 1200px;
    height: 1001px;
    background: var(--stage);
  }
  .bag-front {
    position: absolute;
    left: 210px;
    top: 10px;
    width: 780px;
    height: 981px;
  }
  .bag-art { display: block; width: 100%; height: 100%; }
  .product-name {
    font-family: "Poiret One", sans-serif;
    font-size: 54px;
    letter-spacing: 26px;
    fill: var(--ink);
  }
  .category {
    font-family: "Advent Pro", sans-serif;
    font-weight: 400;
    font-size: 23px;
    letter-spacing: 3px;
    fill: var(--ink);
  }
  .brand-name {
    font-family: "Advent Pro", sans-serif;
    font-weight: 600;
    font-size: 13px;
    letter-spacing: 1px;
    fill: var(--ink);
  }
  .series-name {
    font-family: "Advent Pro", sans-serif;
    font-weight: 300;
    font-size: 26px;
    letter-spacing: 4px;
    fill: var(--ink);
  }
  .brand-square { fill: none; stroke: var(--ink); stroke-width: 2; }
</style>
</head>
<body>
<main class="canvas">
  <section class="bag-front">
    <svg class="bag-art" viewBox="0 0 780 981" xmlns="http://www.w3.org/2000/svg">
      <defs>
        <linearGradient id="outerBand" x1="0" y1="0" x2="0" y2="1">
          <stop offset="0" stop-color="#4a1d7a"/>
          <stop offset="1" stop-color="#3a1668"/>
        </linearGradient>
        <linearGradient id="brightBand" x1="0" y1="0" x2="0" y2="1">
          <stop offset="0" stop-color="#a43fcf"/>
          <stop offset="0.5" stop-color="#7a2fa8"/>
          <stop offset="1" stop-color="#4e2282"/>
        </linearGradient>
        <linearGradient id="facetBand" x1="0" y1="0" x2="0" y2="1">
          <stop offset="0" stop-color="#7c3aa8"/>
          <stop offset="1" stop-color="#5c2a8e"/>
        </linearGradient>
        <linearGradient id="shadowBand" x1="0" y1="0" x2="0" y2="1">
          <stop offset="0" stop-color="#6a2f96"/>
          <stop offset="1" stop-color="#2c1252"/>
        </linearGradient>
        <linearGradient id="centrePanel" x1="0" y1="0" x2="0" y2="1">
          <stop offset="0" stop-color="#8d3db5"/>
          <stop offset="0.35" stop-color="#bd86d2"/>
          <stop offset="0.58" stop-color="#e5c6ec"/>
          <stop offset="0.8" stop-color="#b58ad0"/>
          <stop offset="1" stop-color="#7a45a8"/>
        </linearGradient>
        <linearGradient id="darkEdge" x1="0" y1="0" x2="1" y2="0">
          <stop offset="0" stop-color="#35145f"/>
          <stop offset="1" stop-color="#1f0b40"/>
        </linearGradient>
      </defs>

      <!-- base -->
      <rect width="780" height="981" fill="url(#outerBand)"/>
      <!-- left outer edge -->
      <rect x="0" y="0" width="86" height="981" fill="#3d1870"/>
      <!-- left bright band -->
      <polygon points="86,0 175,0 130,981 86,981" fill="url(#brightBand)"/>
      <!-- left facet -->
      <polygon points="175,0 275,0 212,975 120,981" fill="url(#facetBand)"/>
      <!-- left light seam -->
      <polygon points="178,0 184,0 128,981 122,981" fill="#c58ee0" opacity="0.55"/>
      <!-- left shadow wedge -->
      <polygon points="240,0 275,0 350,545 212,975 200,975" fill="url(#shadowBand)" opacity="0.85"/>

      <!-- right shadow wedge -->
      <polygon points="493,0 540,0 575,975 533,975 447,556" fill="url(#shadowBand)"/>
      <!-- right facet -->
      <polygon points="540,0 556,0 620,981 575,981" fill="#5e2a90"/>
      <!-- right bright band -->
      <polygon points="556,0 688,0 688,981 620,981" fill="url(#brightBand)"/>
      <!-- right outer edge -->
      <rect x="688" y="0" width="92" height="981" fill="url(#darkEdge)"/>

      <!-- centre panel -->
      <polygon points="275,0 493,0 447,556 533,975 212,975 350,545" fill="url(#centrePanel)"/>
      <!-- centre panel light rims -->
      <polyline points="275,0 350,545 212,975" fill="none" stroke="#eed7f3" stroke-width="4" opacity="0.7"/>
      <polyline points="493,0 447,556 533,975" fill="none" stroke="#eed7f3" stroke-width="4" opacity="0.7"/>

      <!-- vertical product name -->
      <text class="product-name" transform="translate(390 672) rotate(-90)" text-anchor="start">PELUND</text>

      <!-- category -->
      <text class="category" x="376" y="736" text-anchor="middle">CAR AIR</text>
      <text class="category" x="376" y="765" text-anchor="middle">FRESHNERS</text>

      <!-- brand -->
      <rect class="brand-square" x="360" y="806" width="32" height="32"/>
      <text class="brand-name" x="376" y="866" text-anchor="middle">LANTERN OF MERIDIA</text>

      <!-- series -->
      <text class="series-name" x="376" y="937" text-anchor="middle">TIDAL SERIES</text>
    </svg>
  </section>
</main>
</body>
</html>
```